Need some visual "dash" to a dashboard UI design

Have a project that needs a little visual "zip". Attached are some screenshots of the current design. Will need source files of design work, Photoshop preferred, but Illustrator or other source will be acceptable. Please confirm before starting the work.

Here is a working prototype:
https://qmv82t.plotvane.example/#g=1&p=scenario_1_-_dashboard_view

Work has been done to get the UI elements in place, but need a little visual improvement to make it really "pop" ...while retaining its usability.

Primarily need some visual design done for the left column 5 elements revealing values for tech in and tech out between 0 and 20. Auth OT values are 0min, 30min, 60min, 90min, 120min, and "over 2 hours". Avail Reserve Capacity will be 0% through 10%. And Supply Delta can range from -10,000 to +10,000

Some design for the charts on the right would be great. Just trying to establish a visual language to apply to these values.

Please use colors from the approved palette with hex values (plus black and white):

Primary
Orange ff7200
Orange Highlight fcb314
Blue 067ab4
Blue Highlight 3aa5dc

Secondary
Lime b6bf00
Lime Highlight dbd810
Green 6ebb1f
Green Highlight c4d82d
Burgundy b30a3c
Burgundy Highlight da3872
Purple 81017e
Purple Highlight b8509e
Dark Blue 0c2577
Dark Blue Highlight 020bb3

Accent
Ochre eaab00
Magenta ff0066
Royal Blue 000066
Yellow ffef00
Teal 00c7b2
Dusty Blue 96b1d0
Light Blue bcc9d6
Mint Green 99ffcc
Gold ff9900
Taupe cccc66
Warm Gray cccc99

Industry/Entity Type

Work

Number of Pages Required

2 page

Font styles to use
Sans Serif

Requirements
Must have
• Must conform to the overall page layout described in the design doc attached. Must conform to the corporate color palette attached in the description.
• sorry, forgot to mention font: must use Verdana
• Verdana Font Family
• Verdana Regular
• Verdana Italic
• Verdana Bold
• Verdana Bold Italic

```html
<!DOCTYPE html>
<html lang="en">
<head>
<meta charset="utf-8">
<title>Capacity Planning · Dashboard</title>
<link rel="stylesheet" href="https://fonts.googleapis.com/css2?family=Open+Sans:wght@400;600;700&display=swap">
<style>
:root{
  --orange:#ff7200;
  --orange-hi:#fcb314;
  --blue:#067ab4;
  --blue-hi:#3aa5dc;
  --lime:#b6bf00;
  --lime-hi:#dbd810;
  --green:#6ebb1f;
  --green-hi:#c4d82d;
  --burgundy:#b30a3c;
  --burgundy-hi:#da3872;
  --purple:#81017e;
  --purple-hi:#b8509e;
  --dark-blue:#0c2577;
  --ochre:#eaab00;
  --magenta:#ff0066;
  --dusty:#96b1d0;
  --light-blue:#bcc9d6;
  --nav:#1566b3;
  --nav-dark:#0d559c;
  --subnav:#0b5aa6;
  --band:#b9ddf3;
  --line:#dcdcdc;
  --text:#222;
  --white:#fff;
}
*{box-sizing:border-box;margin:0;padding:0}
html,body{width:1200px;height:731px;overflow:hidden;background:var(--white)}
body{position:relative;font-family:Verdana,"Open Sans",sans-serif;color:var(--text)}
.abs{position:absolute}

/* top navigation */
.topbar{position:absolute;left:0;top:0;width:1200px;height:50px;background:linear-gradient(180deg,#1a70bf,var(--nav))}
.brand{position:absolute;left:14px;top:12px;display:flex;align-items:center;gap:7px;color:var(--white);font-size:16px;font-weight:700;letter-spacing:.5px}
.brand-dot{width:24px;height:24px;border-radius:50%;background:var(--white)}
.module-tab{position:absolute;top:0;height:50px;color:var(--white);font-size:9px;text-align:center}
.module-tab svg{display:block;margin:8px auto 4px}
.module-tab.is-active{left:128px;width:104px;background:var(--nav-dark);border-top:2px solid var(--orange-hi)}
.module-tab.more{left:240px;width:44px}
.subnav{position:absolute;left:0;top:50px;width:1200px;height:21px;background:var(--subnav)}
.subnav a{position:absolute;top:4px;color:var(--white);font-size:9px;text-decoration:none;transform:translateX(-50%);white-space:nowrap}
.subnav a.is-current{top:3px;left:25px;width:86px;transform:none;text-align:center;border:1px solid var(--white);padding:0 0 1px}

/* left actions panel */
.actions{position:absolute;left:17px;top:84px;width:376px;height:580px;border:1px solid var(--line);background:#fafbfc}
.actions-label{position:absolute;left:12px;top:20px;font-size:9px}
.select{position:absolute;border:1px solid var(--line);background:var(--white);font-size:9px}
.select.site{left:70px;top:13px;width:293px;height:24px;padding:6px 8px;color:var(--orange)}
.caret{position:absolute;right:6px;top:5px;font-size:7px;line-height:6px;color:#444}
.tabs{position:absolute;left:12px;top:54px;width:351px;height:26px;display:flex;border:1px solid var(--line);background:var(--white)}
.tab{font-size:8px;font-weight:700;display:flex;align-items:center;justify-content:center}
.tab.is-active{width:171px;background:var(--blue);color:var(--white)}
.tab.review{flex:1;color:#333}
.days{position:absolute;left:12px;top:80px;width:351px;height:37px;display:flex;background:var(--white)}
.day{position:relative;text-align:center;font-size:9px;padding-top:9px}
.day small{display:block;font-size:7px;color:#555;margin-top:6px}
.day::after{content:"";position:absolute;left:12px;right:12px;top:23px;border-top:1px solid #555}
.day.is-today{width:81px;background:linear-gradient(180deg,var(--blue-hi),#2a93cc);color:var(--white);font-weight:700}
.day.is-today small{color:var(--white);font-weight:400}
.day.is-today::after{border-color:#e9f6ff}
.day.std{flex:1}
.row-band{position:absolute;left:0;top:306px;width:374px;height:82px;background:linear-gradient(90deg,#b3dbf4,#d4ecfa);border-left:4px solid var(--blue)}
.divider{position:absolute;left:15px;width:348px;border-top:1px solid var(--line)}

.site-row{position:absolute;left:0;width:374px;height:70px}
.site-name{position:absolute;left:14px;top:0;font-size:9px;font-weight:700;color:var(--dark-blue)}
.flags{position:absolute;right:12px;top:-2px;display:flex;gap:4px}
.flag{font-size:5px;font-weight:700;color:var(--white);padding:2px 4px;letter-spacing:.2px;border-radius:2px}
.flag.closed{background:var(--burgundy)}
.flag.open{background:var(--green);font-size:6px}
.flag.rollback{background:var(--green)}
.flag.reverse{background:var(--dark-blue)}

.tile{position:absolute;top:18px;height:49px;background:var(--white);border:1px solid #e6e9ee;border-top:3px solid var(--accent);border-radius:3px;box-shadow:0 2px 4px rgba(12,37,119,.08)}
.tile-label{position:absolute;left:0;right:0;top:5px;text-align:center;font-size:7.5px;font-weight:700;color:#444}
.tile-body{position:absolute;left:0;right:0;top:20px;display:flex;align-items:center;justify-content:center;gap:4px}
.tile.in{left:15px;width:52px;--accent:var(--lime)}
.tile.out{left:75px;width:44px;--accent:var(--dusty)}
.tile.ot{left:126px;width:70px;--accent:var(--purple-hi)}
.tile.rsv{left:209px;width:70px;--accent:var(--ochre)}
.tile.delta{left:294px;width:69px}
.tile.delta.neg{--accent:var(--burgundy)}
.tile.delta.pos{--accent:var(--blue)}
.icon-chip{width:17px;height:17px;border-radius:50%;display:flex;align-items:center;justify-content:center}
.chip-in{background:#f3f5d0}
.chip-out{background:#e9eff6}
.chip-ot{background:#fde3ee}
.chip-rsv{background:#fcf1cc}
.chip-neg{background:var(--burgundy)}
.chip-pos{background:var(--blue)}
.val-in{color:var(--lime);font-size:10px;font-weight:700}
.val-rsv{color:var(--ochre);font-size:9px;font-weight:700}
.val-neg{color:var(--burgundy);font-size:9px;font-weight:700}
.val-pos{color:var(--blue);font-size:9px;font-weight:700}
.ot-meter{display:flex;flex-direction:column;gap:2px}
.ot-meter small{font-size:5.5px;color:var(--purple);font-weight:700}
.ot-bar{width:39px;height:6px;border-radius:3px;background:
  repeating-linear-gradient(90deg,transparent 0 7px,#fff 7px 8px),
  linear-gradient(90deg,var(--purple-hi),var(--purple)) 0 0/31px 100% no-repeat,
  #efe4ef}
.rsv-meter{display:flex;flex-direction:column;gap:2px}
.rsv-bar{width:40px;height:5px;border-radius:3px;background:
  repeating-linear-gradient(90deg,transparent 0 3px,#fff 3px 4px),
  #f4e9c7}

/* filter band */
.filters{position:absolute;left:415px;top:86px;width:772px;height:55px;background:var(--band)}
.link{position:absolute;font-size:9px;color:var(--blue);text-decoration:underline}
.select.view{left:6px;top:29px;width:267px;height:19px;padding:3px 8px;font-size:10px;color:#000;border-color:#999;border-radius:2px}
.date-input{position:absolute;top:26px;height:22px;background:var(--white);font-size:12px;padding:3px 10px;letter-spacing:.5px}
.date-input svg{position:absolute;right:6px;top:4px}
.date-input.today{left:304px;width:160px}
.date-input.range{left:495px;width:161px;color:#d4dde3;border:1px solid #dce6ec;background:#f4f9fc}
.checkbox{position:absolute;left:497px;top:10px;display:flex;align-items:center;gap:5px;font-size:9px;color:#333}
.checkbox i{width:9px;height:9px;border:1px solid #888;background:var(--white);border-radius:2px}
.view-switch{position:absolute;left:717px;top:10px;width:1px;height:35px;background:#8aa9be}

/* dashboard */
.dashboard{position:absolute;left:416px;top:151px;width:771px;height:295px;border:1px solid #888;background:var(--white)}
.dashboard h1{position:absolute;left:21px;top:11px;font-size:18px;font-weight:700;color:var(--dark-blue)}
.chart-box{position:absolute;border:1px solid var(--line);border-radius:3px;background:var(--white)}

/* cards */
.card{position:absolute;top:467px;width:175px;height:172px;border:1px solid #d4d8de;border-radius:4px;background:var(--white);box-shadow:0 2px 5px rgba(12,37,119,.12)}
.card svg{position:absolute;left:0;top:0}
.card.fill{left:415px}
.card.installs{left:615px}
.card.duration{left:815px}
.card.commit{left:1013px}

.progress{position:absolute;left:415px;top:656px;width:772px;height:11px;background:#ececec}
.progress span{position:absolute;left:0;top:0;width:522px;height:11px;background:var(--white);border:1px solid #777}
</style>
</head>
<body>

<svg width="0" height="0" style="position:absolute" aria-hidden="true">
  <defs>
    <symbol id="person" viewBox="0 0 14 12"><circle cx="5" cy="3" r="2.6"/><path d="M0 12c0-4 2-6 5-6s5 2 5 6z"/><path d="M9 5h5v2H9z"/></symbol>
    <symbol id="alarm" viewBox="0 0 14 14"><circle cx="7" cy="8" r="5" fill="none" stroke="currentColor" stroke-width="1.6"/><path d="M7 5v3.5h2.5" fill="none" stroke="currentColor" stroke-width="1.4"/><path d="M1 3l3-2M13 3l-3-2" stroke="currentColor" stroke-width="1.4"/></symbol>
    <symbol id="up" viewBox="0 0 10 10"><path d="M5 1.5L9 8.5H1z" fill="currentColor"/></symbol>
    <symbol id="down" viewBox="0 0 10 10"><path d="M5 8.5L9 1.5H1z" fill="currentColor"/></symbol>
    <symbol id="clock" viewBox="0 0 10 10"><circle cx="5" cy="5" r="4" fill="none" stroke="currentColor" stroke-width="1"/><path d="M5 2.5V5h2" fill="none" stroke="currentColor" stroke-width="1"/></symbol>
    <symbol id="cal" viewBox="0 0 14 14"><rect x="1" y="2.5" width="12" height="10.5" fill="none" stroke="currentColor" stroke-width="1.4"/><path d="M1 5.5h12M4 1v3M10 1v3" stroke="currentColor" stroke-width="1.4"/><path d="M4.5 9l2 2 3.5-4" fill="none" stroke="currentColor" stroke-width="1.3"/></symbol>
    <linearGradient id="g-blue" x1="0" y1="0" x2="0" y2="1"><stop offset="0" stop-color="#3aa5dc"/><stop offset="1" stop-color="#067ab4"/></linearGradient>
    <linearGradient id="g-orange" x1="0" y1="0" x2="0" y2="1"><stop offset="0" stop-color="#fcb314"/><stop offset="1" stop-color="#ff7200"/></linearGradient>
    <linearGradient id="g-burgundy" x1="0" y1="0" x2="0" y2="1"><stop offset="0" stop-color="#da3872"/><stop offset="1" stop-color="#b30a3c"/></linearGradient>
    <linearGradient id="g-navy" x1="0" y1="0" x2="0" y2="1"><stop offset="0" stop-color="#067ab4"/><stop offset="1" stop-color="#0c2577"/></linearGradient>
    <linearGradient id="g-hbar-o" x1="0" y1="0" x2="1" y2="0"><stop offset="0" stop-color="#ff7200"/><stop offset="1" stop-color="#fcb314"/></linearGradient>
    <linearGradient id="g-hbar-b" x1="0" y1="0" x2="1" y2="0"><stop offset="0" stop-color="#067ab4"/><stop offset="1" stop-color="#3aa5dc"/></linearGradient>
    <linearGradient id="g-ring" x1="0" y1="0" x2="1" y2="1"><stop offset="0" stop-color="#c4d82d"/><stop offset="1" stop-color="#6ebb1f"/></linearGradient>
    <linearGradient id="g-area" x1="0" y1="0" x2="0" y2="1"><stop offset="0" stop-color="#3aa5dc" stop-opacity=".28"/><stop offset="1" stop-color="#3aa5dc" stop-opacity="0"/></linearGradient>
  </defs>
</svg>

<!-- top navigation -->
<header class="topbar">
  <div class="brand"><span class="brand-dot"></span>KESTREL</div>
  <div class="module-tab is-active">
    <svg width="30" height="18" viewBox="0 0 30 18"><path d="M4 12L26 6" stroke="#fcb314" stroke-width="2.5"/><path d="M15 9l-4 8h8z" fill="#fff"/><rect x="5" y="5" width="6" height="5" fill="#fff"/><rect x="20" y="1" width="5" height="4" fill="#fcb314"/></svg>
    Capacity Planning
  </div>
  <div class="module-tab more">
    <svg width="20" height="20" viewBox="0 0 20 20"><circle cx="10" cy="10" r="8.5" fill="none" stroke="#fff" stroke-width="1.6"/><circle cx="6" cy="10" r="1.4" fill="#fff"/><circle cx="10" cy="10" r="1.4" fill="#fff"/><circle cx="14" cy="10" r="1.4" fill="#fff"/></svg>
    More
  </div>
</header>
<nav class="subnav">
  <a class="is-current" href="#">Dashboard</a>
  <a href="#" style="left:172px">Lights</a>
  <a href="#" style="left:278px">Daily Plan</a>
  <a href="#" style="left:385px">Long Term Plan</a>
  <a href="#" style="left:527px">Schedule Recommendation</a>
  <a href="#" style="left:667px">Config</a>
</nav>

<!-- actions panel -->
<aside class="actions">
  <span class="actions-label">Actions for</span>
  <div class="select site">East Mountain Shores<span class="caret">&#708;<br>&#709;</span></div>

  <div class="tabs">
    <div class="tab is-active">Action Required [4]</div>
    <div class="tab review">Review Required [9]</div>
  </div>
  <div class="days">
    <div class="day is-today">Today<small>03.12</small></div>
    <div class="day std">Tomorrow<small>03.13</small></div>
    <div class="day std">+2<small>03.14</small></div>
    <div class="day std">+3<small>03.15</small></div>
  </div>

  <div class="row-band"></div>
  <div class="divider" style="top:292px"></div>
  <div class="divider" style="top:483px"></div>

  <!-- row 1 -->
  <section class="site-row" style="top:138px">
    <span class="site-name">NSVL_PARIS_CB</span>
    <div class="flags"><span class="flag closed">CLOSED</span></div>
    <div class="tile in"><span class="tile-label">In</span><div class="tile-body"><span class="icon-chip chip-in"><svg width="12" height="10" fill="#b6bf00"><use href="#person"/></svg></span><span class="val-in">+10</span></div></div>
    <div class="tile out"><span class="tile-label">Out</span><div class="tile-body"><span class="icon-chip chip-out"><svg width="12" height="10" fill="#96b1d0"><use href="#person"/></svg></span></div></div>
    <div class="tile ot"><span class="tile-label">Auth OT</span><div class="tile-body"><span class="icon-chip chip-ot"><svg width="11" height="11" style="color:var(--magenta)"><use href="#alarm"/></svg></span><div class="ot-meter"><small>120min</small><span class="ot-bar"></span></div></div></div>
    <div class="tile rsv"><span class="tile-label">Avail Rsv Cap</span><div class="tile-body"><span class="icon-chip chip-rsv"><svg width="12" height="10" fill="#eaab00"><use href="#person"/></svg></span><div class="rsv-meter"><span class="val-rsv">0%</span><span class="rsv-bar"></span></div></div></div>
    <div class="tile delta neg"><span class="tile-label">Supply Delta</span><div class="tile-body"><span class="icon-chip chip-neg"><svg width="9" height="9" style="color:#fff"><use href="#down"/></svg></span><span class="val-neg">-3,390</span></div></div>
  </section>

  <!-- row 2 -->
  <section class="site-row" style="top:220px">
    <span class="site-name">NSVL_PARIS_CB</span>
    <div class="flags"><span class="flag closed">CLOSED</span></div>
    <div class="tile in"><span class="tile-label">In</span><div class="tile-body"><span class="icon-chip chip-in"><svg width="12" height="10" fill="#b6bf00"><use href="#person"/></svg></span><span class="val-in">+10</span></div></div>
    <div class="tile out"><span class="tile-label">Out</span><div class="tile-body"><span class="icon-chip chip-out"><svg width="12" height="10" fill="#96b1d0"><use href="#person"/></svg></span></div></div>
    <div class="tile ot"><span class="tile-label">Auth OT</span><div class="tile-body"><span class="icon-chip chip-ot"><svg width="11" height="11" style="color:var(--magenta)"><use href="#alarm"/></svg></span><div class="ot-meter"><small>120min</small><span class="ot-bar"></span></div></div></div>
    <div class="tile rsv"><span class="tile-label">Avail Rsv Cap</span><div class="tile-body"><span class="icon-chip chip-rsv"><svg width="12" height="10" fill="#eaab00"><use href="#person"/></svg></span><div class="rsv-meter"><span class="val-rsv">0%</span><span class="rsv-bar"></span></div></div></div>
    <div class="tile delta neg"><span class="tile-label">Supply Delta</span><div class="tile-body"><span class="icon-chip chip-neg"><svg width="9" height="9" style="color:#fff"><use href="#down"/></svg></span><span class="val-neg">-3,390</span></div></div>
  </section>

  <!-- row 3 (selected) -->
  <section class="site-row" style="top:316px">
    <span class="site-name">NSVL_PARIS_CB</span>
    <div class="flags"><span class="flag rollback">Roll Back</span><span class="flag reverse">Utilize Reverse Capacity</span><span class="flag closed">CLOSED</span></div>
    <div class="tile in"><span class="tile-label">In</span><div class="tile-body"><span class="icon-chip chip-in"><svg width="12" height="10" fill="#b6bf00"><use href="#person"/></svg></span><span class="val-in">+10</span></div></div>
    <div class="tile out"><span class="tile-label">Out</span><div class="tile-body"><span class="icon-chip chip-out"><svg width="12" height="10" fill="#96b1d0"><use href="#person"/></svg></span></div></div>
    <div class="tile ot"><span class="tile-label">Auth OT</span><div class="tile-body"><span class="icon-chip chip-ot"><svg width="11" height="11" style="color:var(--magenta)"><use href="#alarm"/></svg></span><div class="ot-meter"><small>120min</small><span class="ot-bar"></span></div></div></div>
    <div class="tile rsv"><span class="tile-label">Avail Rsv Cap</span><div class="tile-body"><span class="icon-chip chip-rsv"><svg width="12" height="10" fill="#eaab00"><use href="#person"/></svg></span><div class="rsv-meter"><span class="val-rsv">0%</span><span class="rsv-bar"></span></div></div></div>
    <div class="tile delta pos"><span class="tile-label">Supply Delta</span><div class="tile-body"><span class="icon-chip chip-pos"><svg width="9" height="9" style="color:#fff"><use href="#up"/></svg></span><span class="val-pos">+180</span></div></div>
  </section>

  <!-- row 4 -->
  <section class="site-row" style="top:406px">
    <span class="site-name">NSVL_PARIS_CB</span>
    <div class="flags"><span class="flag open">OPEN</span></div>
    <div class="tile in"><span class="tile-label">In</span><div class="tile-body"><span class="icon-chip chip-in"><svg width="12" height="10" fill="#b6bf00"><use href="#person"/></svg></span><span class="val-in">+10</span></div></div>
    <div class="tile out"><span class="tile-label">Out</span><div class="tile-body"><span class="icon-chip chip-out"><svg width="12" height="10" fill="#96b1d0"><use href="#person"/></svg></span></div></div>
    <div class="tile ot"><span class="tile-label">Auth OT</span><div class="tile-body"><span class="icon-chip chip-ot"><svg width="11" height="11" style="color:var(--magenta)"><use href="#alarm"/></svg></span><div class="ot-meter"><small>120min</small><span class="ot-bar"></span></div></div></div>
    <div class="tile rsv"><span class="tile-label">Avail Rsv Cap</span><div class="tile-body"><span class="icon-chip chip-rsv"><svg width="12" height="10" fill="#eaab00"><use href="#person"/></svg></span><div class="rsv-meter"><span class="val-rsv">0%</span><span class="rsv-bar"></span></div></div></div>
    <div class="tile delta pos"><span class="tile-label">Supply Delta</span><div class="tile-body"><span class="icon-chip chip-pos"><svg width="9" height="9" style="color:#fff"><use href="#up"/></svg></span><span class="val-pos">+3,390</span></div></div>
  </section>

  <!-- row 5 -->
  <section class="site-row" style="top:497px">
    <span class="site-name">NSVL_PARIS_CB</span>
    <div class="flags"><span class="flag open">OPEN</span></div>
    <div class="tile in"><span class="tile-label">In</span><div class="tile-body"><span class="icon-chip chip-in"><svg width="12" height="10" fill="#b6bf00"><use href="#person"/></svg></span><span class="val-in">+10</span></div></div>
    <div class="tile out"><span class="tile-label">Out</span><div class="tile-body"><span class="icon-chip chip-out"><svg width="12" height="10" fill="#96b1d0"><use href="#person"/></svg></span></div></div>
    <div class="tile ot"><span class="tile-label">Auth OT</span><div class="tile-body"><span class="icon-chip chip-ot"><svg width="11" height="11" style="color:var(--magenta)"><use href="#alarm"/></svg></span><div class="ot-meter"><small>120min</small><span class="ot-bar"></span></div></div></div>
    <div class="tile rsv"><span class="tile-label">Avail Rsv Cap</span><div class="tile-body"><span class="icon-chip chip-rsv"><svg width="12" height="10" fill="#eaab00"><use href="#person"/></svg></span><div class="rsv-meter"><span class="val-rsv">0%</span><span class="rsv-bar"></span></div></div></div>
    <div class="tile delta pos"><span class="tile-label">Supply Delta</span><div class="tile-body"><span class="icon-chip chip-pos"><svg width="9" height="9" style="color:#fff"><use href="#up"/></svg></span><span class="val-pos">+ 526</span></div></div>
  </section>
</aside>

<!-- filter band -->
<div class="filters">
  <span class="link" style="left:8px;top:11px">Previously viewed</span>
  <div class="select view">NSVL_PARIS_CB<span class="caret" style="top:3px;color:#000">&#9650;<br>&#9660;</span></div>
  <span class="link" style="left:304px;top:11px">Today</span>
  <div class="date-input today">03.12.2018<svg width="14" height="14" style="color:#333"><use href="#cal"/></svg></div>
  <div class="checkbox"><i></i>Show date range</div>
  <div class="date-input range">03.05.2018<svg width="14" height="14" style="color:#d4dde3"><use href="#cal"/></svg></div>
  <svg class="abs" style="left:689px;top:18px" width="24" height="20" viewBox="0 0 24 20"><path d="M2 1v17h21" fill="none" stroke="#24476b" stroke-width="2"/><path d="M7 16V9M11 16V5M15 16V8M19 16V3" stroke="#24476b" stroke-width="2.4"/></svg>
  <span class="view-switch"></span>
  <svg class="abs" style="left:727px;top:17px" width="30" height="22" viewBox="0 0 30 22"><path d="M2 4l8-3 9 3 9-3v17l-9 3-9-3-8 3z M10 1v17 M19 4v17" fill="none" stroke="#6b7f92" stroke-width="2" stroke-linejoin="round"/></svg>
</div>

<!-- dashboard -->
<main class="dashboard">
  <h1>Dashboard</h1>

  <div class="chart-box" style="left:11px;top:54px;width:436px;height:229px">
    <svg width="436" height="229" viewBox="0 0 436 229" font-family="Verdana, 'Open Sans', sans-serif">
      <text x="218" y="19" text-anchor="middle" font-size="10" fill="#333">Intakes vs Completions</text>
      <g stroke="#e9ecf0" stroke-width="1">
        <line x1="25" y1="33" x2="425" y2="33"/><line x1="25" y1="61" x2="425" y2="61"/><line x1="25" y1="89" x2="425" y2="89"/><line x1="25" y1="117" x2="425" y2="117"/><line x1="25" y1="145" x2="425" y2="145"/><line x1="25" y1="173" x2="425" y2="173" stroke="#b5bcc6"/>
      </g>
      <g font-size="6.5" fill="#444" text-anchor="end">
        <text x="19" y="35">250</text><text x="19" y="63">200</text><text x="19" y="91">150</text><text x="19" y="119">100</text><text x="19" y="147">50</text><text x="19" y="175">0</text>
      </g>
      <g font-size="6" fill="#444" text-anchor="end">
        <text transform="translate(36 181) rotate(-45)">2/27/18</text>
        <text transform="translate(55 181) rotate(-45)">2/28/18</text>
        <text transform="translate(74 181) rotate(-45)">3/1/18</text>
        <text transform="translate(93 181) rotate(-45)">3/2/18</text>
        <text transform="translate(112 181) rotate(-45)">3/3/18</text>
        <text transform="translate(131 181) rotate(-45)">3/4/18</text>
        <text transform="translate(150 181) rotate(-45)">3/5/18</text>
        <text transform="translate(170 181) rotate(-45)">3/6/18</text>
        <text transform="translate(189 181) rotate(-45)">3/7/18</text>
        <text transform="translate(208 181) rotate(-45)">3/8/18</text>
        <text transform="translate(227 181) rotate(-45)">3/9/18</text>
        <text transform="translate(246 181) rotate(-45)">3/10/18</text>
        <text transform="translate(265 181) rotate(-45)">3/11/18</text>
        <text transform="translate(285 181) rotate(-45)">3/12/18</text>
        <text transform="translate(304 181) rotate(-45)">3/13/18</text>
        <text transform="translate(323 181) rotate(-45)">3/14/18</text>
        <text transform="translate(342 181) rotate(-45)">3/15/18</text>
        <text transform="translate(361 181) rotate(-45)">3/16/18</text>
        <text transform="translate(380 181) rotate(-45)">3/17/18</text>
        <text transform="translate(399 181) rotate(-45)">3/18/18</text>
        <text transform="translate(419 181) rotate(-45)">3/19/18</text>
      </g>
      <polygon fill="url(#g-area)" points="34,114.2 53.2,117 72.3,105.8 91.5,115.3 110.6,107.5 129.8,113.6 148.9,111.4 168.1,115.9 187.2,111.4 206.4,111.4 225.5,115.3 244.7,115.3 263.8,105.8 283,118.1 302.1,116.4 321.3,116.4 340.4,114.2 359.6,111.4 378.7,106.9 397.9,108.6 417,111.4 417,173 34,173"/>
      <g fill="none" stroke-width="2" stroke-linejoin="round" stroke-linecap="round">
        <polyline stroke="#96b1d0" points="34,54.3 53.2,57.1 72.3,58.2 91.5,62.1 110.6,57.1 129.8,67.7 148.9,55.4 168.1,70.5 187.2,70.5 206.4,68.3 225.5,70.5 244.7,70.5 263.8,50.9 283,55.4 302.1,71.1 321.3,50.9 340.4,66.6 359.6,55.4 378.7,71.1 397.9,50.9 417,62.7"/>
        <polyline stroke="#fcb314" points="34,61 53.2,59.3 72.3,47 91.5,47 110.6,59.9 129.8,44.2 148.9,45.9 168.1,57.1 187.2,45.3 206.4,59.9 225.5,47 244.7,48.7 263.8,55.4"/>
        <polyline stroke="#067ab4" points="34,114.2 53.2,117 72.3,105.8 91.5,115.3 110.6,107.5 129.8,113.6 148.9,111.4 168.1,115.9 187.2,111.4 206.4,111.4 225.5,115.3 244.7,115.3 263.8,105.8 283,118.1 302.1,116.4 321.3,116.4 340.4,114.2 359.6,111.4 378.7,106.9 397.9,108.6 417,111.4"/>
        <polyline stroke="#ff7200" points="34,111.4 53.2,111.4 72.3,117 91.5,117 110.6,117 129.8,173 148.9,105.8 168.1,110.3 187.2,112.5 206.4,117 225.5,117 244.7,117 263.8,173"/>
      </g>
      <g stroke="#fff" stroke-width="1.2">
        <circle cx="417" cy="111.4" r="2.6" fill="#067ab4"/><circle cx="417" cy="62.7" r="2.6" fill="#96b1d0"/>
        <circle cx="263.8" cy="55.4" r="2.6" fill="#fcb314"/><circle cx="263.8" cy="173" r="2.6" fill="#ff7200"/>
      </g>
      <g font-size="6.5" fill="#444">
        <line x1="52" y1="219" x2="62" y2="219" stroke="#067ab4" stroke-width="2"/><text x="63" y="221.5">Install Intakes</text>
        <line x1="130" y1="219" x2="140" y2="219" stroke="#ff7200" stroke-width="2"/><text x="141" y="221.5">Install Completions</text>
        <line x1="224" y1="219" x2="234" y2="219" stroke="#96b1d0" stroke-width="2"/><text x="235" y="221.5">Repair Intakes</text>
        <line x1="305" y1="219" x2="315" y2="219" stroke="#fcb314" stroke-width="2"/><text x="316" y="221.5">Repair Completions</text>
      </g>
    </svg>
  </div>

  <div class="chart-box" style="left:467px;top:8px;width:265px;height:153px">
    <svg width="265" height="153" viewBox="0 0 265 153" font-family="Verdana, 'Open Sans', sans-serif">
      <text x="132" y="14" text-anchor="middle" font-size="7.5" fill="#333">Technician Breakdown</text>
      <g stroke="#eef0f3"><line x1="69" y1="22" x2="69" y2="133" stroke="#b5bcc6"/><line x1="89.3" y1="22" x2="89.3" y2="133"/><line x1="109.7" y1="22" x2="109.7" y2="133"/><line x1="130" y1="22" x2="130" y2="133"/><line x1="150.4" y1="22" x2="150.4" y2="133"/><line x1="170.7" y1="22" x2="170.7" y2="133"/><line x1="191" y1="22" x2="191" y2="133"/><line x1="211.4" y1="22" x2="211.4" y2="133"/><line x1="231.7" y1="22" x2="231.7" y2="133"/><line x1="252" y1="22" x2="252" y2="133"/></g>
      <g font-size="4.6" fill="#444" text-anchor="end">
        <text x="64" y="31">Available Techs</text><text x="64" y="46">Techs on Proactive Load</text><text x="64" y="62">Loan Out</text><text x="64" y="80">Loan In</text><text x="64" y="96">Assigned to Load</text><text x="64" y="111">Unscheduled Techs</text><text x="64" y="128">Scheduled Techs</text>
      </g>
      <g fill="url(#g-hbar-o)">
        <rect x="69" y="27" width="23.4" height="4" rx="1"/><rect x="69" y="42" width="45.8" height="4" rx="1"/><rect x="69" y="58" width="10.2" height="4" rx="1"/><rect x="69" y="92" width="90.5" height="4" rx="1"/><rect x="69" y="107" width="20.3" height="4" rx="1"/><rect x="69" y="124" width="169.8" height="4" rx="1"/>
      </g>
      <g fill="url(#g-hbar-b)">
        <rect x="69" y="78" width="5.1" height="4" rx="1"/><rect x="69" y="96" width="101.7" height="4" rx="1"/><rect x="69" y="111" width="17.3" height="4" rx="1"/><rect x="69" y="128" width="106.8" height="4" rx="1"/>
      </g>
      <g font-size="4.6" fill="#444">
        <text x="95" y="31">23</text><text x="117" y="46">45</text><text x="81" y="62">10</text><text x="76" y="82">0</text><text x="162" y="95">89</text><text x="92" y="111">20</text><text x="241" y="128">167</text>
      </g>
      <g font-size="4.8" fill="#444" text-anchor="middle">
        <text x="69" y="143">0</text><text x="89.3" y="143">20</text><text x="109.7" y="143">40</text><text x="130" y="143">60</text><text x="150.4" y="143">80</text><text x="170.7" y="143">100</text><text x="191" y="143">120</text><text x="211.4" y="143">140</text><text x="231.7" y="143">160</text><text x="252" y="143">180</text>
      </g>
    </svg>
  </div>

  <div class="chart-box" style="left:467px;top:168px;width:265px;height:115px">
    <svg width="265" height="115" viewBox="0 0 265 115" font-family="Verdana, 'Open Sans', sans-serif">
      <text x="132" y="12" text-anchor="middle" font-size="7.5" fill="#333">Tech Utilization</text>
      <g stroke="#eef0f3"><line x1="69" y1="18" x2="69" y2="89" stroke="#b5bcc6"/><line x1="89.3" y1="18" x2="89.3" y2="89"/><line x1="109.7" y1="18" x2="109.7" y2="89"/><line x1="130" y1="18" x2="130" y2="89"/><line x1="150.4" y1="18" x2="150.4" y2="89"/><line x1="170.7" y1="18" x2="170.7" y2="89"/><line x1="191" y1="18" x2="191" y2="89"/><line x1="211.4" y1="18" x2="211.4" y2="89"/><line x1="231.7" y1="18" x2="231.7" y2="89"/><line x1="252" y1="18" x2="252" y2="89"/></g>
      <g font-size="4.6" fill="#444" text-anchor="end">
        <text x="64" y="28">Available Techs</text><text x="64" y="47">Techs on Proactive work</text><text x="64" y="65">Techs on Load</text><text x="64" y="82">Activated Techs</text>
      </g>
      <g fill="url(#g-hbar-o)"><rect x="69" y="22" width="33.6" height="4" rx="1"/><rect x="69" y="41" width="45.8" height="4" rx="1"/><rect x="69" y="59" width="89.5" height="4" rx="1"/><rect x="69" y="76" width="169.8" height="4" rx="1"/></g>
      <g fill="url(#g-hbar-b)"><rect x="69" y="63" width="101.7" height="4" rx="1"/><rect x="69" y="80" width="101.7" height="4" rx="1"/></g>
      <g font-size="4.8" fill="#444" text-anchor="middle">
        <text x="69" y="98">0</text><text x="89.3" y="98">20</text><text x="109.7" y="98">40</text><text x="130" y="98">60</text><text x="150.4" y="98">80</text><text x="170.7" y="98">100</text><text x="191" y="98">120</text><text x="211.4" y="98">140</text><text x="231.7" y="98">160</text><text x="252" y="98">180</text>
      </g>
      <g font-size="4.2" fill="#444"><rect x="117" y="104" width="3" height="3" fill="#ff7200"/><text x="121" y="107">TFS</text><rect x="131" y="104" width="3" height="3" fill="#067ab4"/><text x="135" y="107">IEFS</text></g>
    </svg>
  </div>
</main>

<!-- fill rate -->
<article class="card fill">
  <svg width="175" height="172" viewBox="0 0 175 172" font-family="Verdana, 'Open Sans', sans-serif">
    <text x="95" y="16" font-size="9" font-weight="700">03.12.2018</text>
    <svg x="155" y="7" width="11" height="11" style="color:#222"><use href="#clock"/></svg>
    <text x="18" y="30" font-size="11" font-weight="700" fill="#0c2577">Fill Rate</text>
    <line x1="8" y1="40" x2="167" y2="40" stroke="#ddd"/>
    <circle cx="88" cy="103" r="51" fill="none" stroke="#c4d82d" stroke-width="1.5"/>
    <path d="M88 52a51 51 0 0 1 37.2 16.1" fill="none" stroke="#6ebb1f" stroke-width="4" stroke-linecap="round"/>
    <circle cx="88" cy="103" r="38" fill="#f3f8ec" stroke="url(#g-ring)" stroke-width="7"/>
    <text x="88" y="111" text-anchor="middle" font-size="20" font-weight="600" fill="#6ebb1f">112%</text>
    <path d="M130 157l3.5-6 3.5 6z" fill="#6ebb1f"/>
    <text x="141" y="157" font-size="10" fill="#333">5,1%</text>
  </svg>
</article>

<!-- installs & repairs -->
<article class="card installs">
  <svg width="175" height="172" viewBox="0 0 175 172" font-family="Verdana, 'Open Sans', sans-serif">
    <rect x="12" y="15" width="6" height="6" rx="1" fill="#0c2577"/><text x="12" y="32" font-size="8.5">Actual</text>
    <rect x="55" y="15" width="6" height="6" rx="1" fill="var(--orange)"/><text x="51" y="32" font-size="8.5">Projected</text>
    <text x="90" y="20" font-size="9" font-weight="700">03.12.2018</text>
    <path d="M157 21h9M159 17l5-5 2 2-5 5h-2z" fill="none" stroke="#222" stroke-width="1"/>
    <text x="13" y="50" font-size="11" font-weight="700" fill="#0c2577">Installs</text>
    <text x="105" y="50" font-size="11" font-weight="700" fill="#0c2577">Repairs</text>
    <line x1="8" y1="58" x2="72" y2="58" stroke="#ddd"/><line x1="90" y1="58" x2="157" y2="58" stroke="#ddd"/>
    <g font-size="8" fill="#222"><text x="7" y="87">120</text><text x="7" y="113">110</text><text x="7" y="138">100</text><text x="9" y="163">90</text><text x="86" y="87">240</text><text x="86" y="113">220</text><text x="86" y="138">200</text><text x="86" y="163">180</text></g>
    <line x1="26" y1="158" x2="58" y2="158" stroke="#b5bcc6"/><line x1="109" y1="158" x2="141" y2="158" stroke="#b5bcc6"/>
    <rect x="29" y="135" width="11" height="23" rx="1.5" fill="url(#g-navy)"/><rect x="42" y="86" width="12" height="72" rx="1.5" fill="url(#g-orange)"/>
    <rect x="112" y="135" width="11" height="23" rx="1.5" fill="url(#g-navy)"/><rect x="126" y="86" width="11" height="72" rx="1.5" fill="url(#g-orange)"/>
  </svg>
</article>

<!-- duration -->
<article class="card duration">
  <svg width="175" height="172" viewBox="0 0 175 172" font-family="Verdana, 'Open Sans', sans-serif">
    <text x="90" y="17" font-size="9" font-weight="700">03.12.2018</text>
    <svg x="160" y="8" width="11" height="11" style="color:#222"><use href="#clock"/></svg>
    <text x="14" y="33" font-size="11" font-weight="700" fill="#0c2577">Duration</text>
    <line x1="8" y1="44" x2="167" y2="44" stroke="#ddd"/>
    <g font-size="8"><text x="11" y="67">185</text><text x="11" y="94">150</text><text x="11" y="118">100</text><text x="15" y="144">50</text></g>
    <line x1="40" y1="140" x2="125" y2="140" stroke="#b5bcc6"/>
    <rect x="49" y="67" width="20" height="73" rx="2" fill="url(#g-burgundy)"/>
    <rect x="92" y="117" width="20" height="23" rx="2" fill="url(#g-blue)"/>
    <rect x="60" y="151" width="6" height="6" rx="1" fill="var(--burgundy)"/><rect x="98" y="151" width="6" height="6" rx="1" fill="var(--blue-hi)"/>
    <g font-size="8.5"><text x="4" y="167">Minutes</text><text x="55" y="167">Install</text><text x="94" y="167">Repair</text></g>
  </svg>
</article>

<!-- tech commit -->
<article class="card commit">
  <svg width="175" height="172" viewBox="0 0 175 172" font-family="Verdana, 'Open Sans', sans-serif">
    <text x="98" y="17" font-size="9" font-weight="700">03.12.2018</text>
    <svg x="160" y="8" width="11" height="11" style="color:#222"><use href="#clock"/></svg>
    <text x="7" y="33" font-size="11" font-weight="700" fill="#0c2577">Tech Commit</text>
    <line x1="7" y1="43" x2="167" y2="43" stroke="#ddd"/>
    <g font-size="8"><text x="10" y="68">110</text><text x="10" y="94">105</text><text x="10" y="119">100</text><text x="13" y="145">95</text></g>
    <line x1="36" y1="140" x2="108" y2="140" stroke="#b5bcc6"/>
    <rect x="44" y="67" width="17" height="73" rx="2" fill="url(#g-burgundy)"/>
    <rect x="82" y="77" width="17" height="63" rx="2" fill="url(#g-blue)"/>
    <rect x="42" y="151" width="6" height="6" rx="1" fill="var(--burgundy)"/><rect x="87" y="151" width="6" height="6" rx="1" fill="var(--blue-hi)"/>
    <g font-size="8.5"><text x="30" y="167">Commit</text><text x="77" y="167">Actual</text></g>
  </svg>
</article>

<div class="progress"><span></span></div>

</body>
</html>
```